Modern and Clean Web Re-Design Project

We have 2 companies in similar industries: Printing and Mail Preparation/Fulfillment. We prefer sites that are clean and easy to navigate.Our printing company, Harbourline Press Works' website, hpwdirect.example is outdated needs revamping. We have rebranded our logo and are looking for a new design that is clean, modern and geared to other corporations and business in the downtown Toronto area. Our mailing company, The Postwick Depot (thepostwickdepot.example) needs a website as well. This company is in the Direct Mail and letter shop business, which essentially is addressing/personalizing people's printed matter and preparing it for either the Canadian or US postal service. The Postwick Depot specializes in not-for-profit and corporate sectors.Please see our logos to get an idea of the colors and look we want. For all intensive purposes, the sites can look similar in design all we want is that each site has the appropriate corporate colors and is a bit different so they don't look identical as the two business run as separate corporations.The content of the website should be easily changed by our staff and we want it to be setup to optimized for SEO based on the keywords we want. We are looking for someone to work on this project immediately
Updates

Project Deadline Extended
Reason: Change of ideas

After doing some thinking, I would like the site to be more modern but the non flash sites that I have seen so far Im finding life-less and while I want something clean, not overly busy and corporate looking, I dont want the design to be bland looking.

Please design with the previous specs in mind but with a twist as mentioned above.

Thanks
Dorian

Target Market(s)

See above

Industry/Entity Type

Printing

Requirements
Must have
• Must match the design and style of each respective logoSee the attached impage of the front of our offices to have an idea of our lookWe must be able to edit the content ourselves without any fancy programs or tools.Must be SEO optimized
Nice to have
• An online order form that can be emailed to us for quotes.....perhaps a page with a bunch of fields that have drop down menus....
Should not have
• Should not be overly busy. I want it to be clean and simple but informative without being hard to navigate

```html
<!DOCTYPE html>
<html lang="en">
<head>
<meta charset="utf-8">
<title>Harbourline Press Works</title>
<link rel="stylesheet" href="https://fonts.googleapis.com/css2?family=Montserrat:wght@300;400;500;600&family=Arimo:wght@400;700&display=swap">
<style>
:root{
  --white:#ffffff;
  --page:#3b3b3b;
  --footer:#414141;
  --ink-light:#dcdcdc;
  --ink-body:#b9b9b9;
  --ink-muted:#9a9a9a;
  --nav-ink:#444444;
  --orange:#f7a52a;
  --red:#f05a30;
  --hero-brown:#8a6d54;
  --hero-brown-dark:#6f5541;
  --slider:#575757;
}
*{margin:0;padding:0;box-sizing:border-box}
html,body{width:1200px;height:1000px;overflow:hidden}
body{position:relative;background:var(--page);font-family:"Arimo",Arial,sans-serif}
.site-header{position:absolute;left:0;top:0;width:1200px;height:92px;background:var(--white);box-shadow:0 3px 6px rgba(0,0,0,.35);z-index:2}
.brand{position:absolute;left:122px;top:22px;display:flex;align-items:center;gap:10px;font-family:"Montserrat",sans-serif;font-weight:500;font-size:17px;line-height:20px;color:var(--red)}
.brand-dot{width:26px;height:26px;border-radius:50%;background:var(--orange);flex:none}
.main-nav{position:absolute;left:412px;top:45px;display:flex;align-items:center;font-family:"Montserrat",sans-serif;font-weight:300;font-size:17px;color:var(--nav-ink)}
.main-nav a{color:inherit;text-decoration:none}
.nav-sep{display:inline-block;width:1px;height:14px;background:#c8c8c8;margin:0 28px}
.phone{display:flex;align-items:center;gap:6px;color:var(--red)}
main{position:absolute;left:0;top:92px;width:1200px;height:778px;background:var(--page)}
.hero{position:absolute;left:121px;top:29px;width:956px;height:393px;box-shadow:0 10px 24px rgba(0,0,0,.5)}
.hero-backdrop{position:absolute;left:0;top:0;width:956px;height:372px;background:linear-gradient(90deg,var(--hero-brown-dark),var(--hero-brown) 45%,#937560)}
.hero-stack{position:absolute;left:0;top:0}
.hero-copy{position:absolute;left:586px;top:104px;font-family:"Montserrat",sans-serif}
.hero-lead{font-weight:300;font-size:33px;line-height:35px;color:var(--white)}
.hero-claim{margin-top:14px;font-weight:600;font-size:41px;line-height:48px;color:var(--orange)}
.hero-band{position:absolute;left:0;width:956px}
.band-orange{top:372px;height:10px;background:var(--orange)}
.band-red{top:382px;height:11px;background:var(--red)}
.slider-dots{position:absolute;left:930px;top:115px;width:35px;height:155px;background:var(--slider);display:flex;flex-direction:column;align-items:center;padding-top:26px;gap:11px}
.slider-dots span{width:12px;height:12px;border-radius:50%;background:var(--white)}
.slider-dots .active{background:var(--orange)}
.mission{position:absolute;left:123px;top:446px;width:445px}
.section-title{font-family:"Montserrat",sans-serif;font-weight:300;font-size:33px;line-height:40px;color:var(--ink-light)}
.mission p{margin-top:28px;font-size:11.6px;line-height:17.4px;color:var(--ink-body);padding-left:1px}
.mission p+p{margin-top:17px}
.service{position:absolute;top:446px;width:216px}
.service-digital{left:611px}
.service-commercial{left:861px}
.service h2{font-family:"Montserrat",sans-serif;font-weight:400;font-size:32px;line-height:38px}
.service h2 small{display:block;font-size:17px;line-height:16px}
.service-digital h2{color:var(--red)}
.service-commercial h2{color:var(--orange)}
.service-image{display:block;margin-top:17px;width:215px;height:114px;box-shadow:0 5px 6px rgba(0,0,0,.5)}
.service p{margin-top:21px;padding-left:3px;width:210px;font-size:11.6px;line-height:14.5px;color:var(--ink-body);height:58px;overflow:hidden}
.read-more{display:inline-block;margin:14px 0 0 5px;padding:1px 6px;background:#2b2b2b;font-size:11px;color:#c0512e;text-decoration:none}
.service-commercial .read-more{color:var(--orange)}
.site-footer{position:absolute;left:0;top:870px;width:1200px;height:130px;background:var(--footer);box-shadow:inset 0 4px 6px rgba(0,0,0,.35)}
.footer-brand{position:absolute;left:124px;top:37px;display:flex;align-items:center;gap:9px;font-family:"Montserrat",sans-serif;font-weight:500;font-size:16px;line-height:19px;color:#8c8c8c}
.footer-brand .brand-dot{background:#777}
.footer-divider{position:absolute;left:310px;top:30px;width:1px;height:72px;background:#5a5a5a}
.footer-address{position:absolute;left:339px;top:28px;font-style:normal;font-size:12px;line-height:17.5px;color:var(--ink-muted)}
.footer-address strong{color:#a8a8a8}
.footer-email{display:block;margin-top:9px}
.socials{position:absolute;right:123px;top:29px;display:flex;gap:6px}
.socials span{width:18px;height:18px;border-radius:50%;background:#8e8e8e}
.footer-nav{position:absolute;right:123px;top:64px;font-size:12px;color:var(--ink-muted)}
.footer-nav a{color:inherit;text-decoration:none}
.footer-nav i{font-style:normal;margin:0 6px}
.copyright{position:absolute;right:123px;top:90px;font-size:12px;color:var(--ink-muted)}
.copyright strong{color:#b3b3b3}
</style>
</head>
<body>
<header class="site-header">
  <div class="brand"><span class="brand-dot"></span>Harbourline<br>Press Works</div>
  <nav class="main-nav">
    <a href="#">About Us</a><span class="nav-sep"></span>
    <a href="#">Services</a><span class="nav-sep"></span>
    <a href="#">Email a File</a><span class="nav-sep"></span>
    <a href="#">Contact</a><span class="nav-sep"></span>
    <span class="phone">
      <svg width="12" height="16" viewBox="0 0 12 16"><path d="M3 1 L5 4 L3.5 6 Q5 10 8 12 L10 10.5 L12 13 L9.5 15.5 Q2 12 0.5 3.5 Z" fill="#f05a30"/></svg>
      416-555-0148
    </span>
  </nav>
</header>

<main>
  <section class="hero">
    <div class="hero-backdrop" role="img" aria-label="Softly blurred warm-toned photo of children as slide background"></div>
    <svg class="hero-stack" width="520" height="372" viewBox="0 0 520 372">
      <g transform="rotate(-4 265 190)">
        <rect x="52" y="58" width="380" height="265" fill="#ffffff"/>
        <rect x="58" y="64" width="368" height="253" fill="#5d8f3c"/>
      </g>
      <g transform="rotate(-2 275 190)">
        <rect x="78" y="62" width="390" height="270" fill="#ffffff"/>
        <rect x="84" y="68" width="378" height="258" fill="#2a6fb8"/>
      </g>
      <g transform="rotate(2 300 200)" role="img" aria-label="Framed photo of three smiling children sitting by a stone wall">
        <rect x="105" y="62" width="390" height="280" fill="#ffffff" filter="drop-shadow(3px 4px 4px rgba(0,0,0,.4))"/>
        <rect x="112" y="69" width="376" height="266" fill="#7c8a5a"/>
      </g>
    </svg>
    <div class="hero-copy">
      <p class="hero-lead">Nothing more to<br>says about us</p>
      <p class="hero-claim">We just print<br>your dream...</p>
    </div>
    <div class="slider-dots"><span class="active"></span><span></span><span></span><span></span><span></span></div>
    <div class="hero-band band-orange"></div>
    <div class="hero-band band-red"></div>
  </section>

  <section class="mission">
    <h1 class="section-title">Our Mission</h1>
    <p>We maintain absolute integrity in every aspect of our operation. By using our experience to understand our customers' expectations, we show an uncommon commitment to achieving a high-quality product under strict deadlines. It is the customers who set the standards we strive to achieve. We are professionals who bring unique and specialized skills you can depend on.We maintain absolute integrity in every aspect of our operation. By using our experience to understand our customers' expectations, we show an uncommon commitment to achieving a high-quality product under strict deadlines. It is the customers who set the standards we strive to achieve.</p>
    <p>every aspect of our operation. By using our experience to understand our customers' expectations, we show an uncommon commitment to achieving a high-quality product under strict deadlines. It is the customers who set the standards.</p>
  </section>

  <section class="service service-digital">
    <h2>Digital<small>Printing</small></h2>
    <div class="service-image" role="img" aria-label="Illustration of colourful cubes in a rainbow spectrum" style="background:linear-gradient(120deg,#2a8fd8 0%,#38b34a 30%,#e8e23a 55%,#f0a21f 72%,#e5241f 90%,#ffffff 100%)"></div>
    <p>HPW offers the latest technology available for photocopies, colour copies and poster printing. All of these services are available on same-day</p>
    <a class="read-more" href="#">Read More &gt;</a>
  </section>

  <section class="service service-commercial">
    <h2>Commercial<small>Printing</small></h2>
    <div class="service-image" role="img" aria-label="Photo of printed brochures, cards and packaging samples" style="background:linear-gradient(120deg,#9ac23c 0%,#e9ebe4 35%,#d8d8d8 60%,#3c2f6a 80%,#2c2c2c 100%)"></div>
    <p>Although we built our reputation on producing copies, we also offer a full range of commercial printing services. We can meet all your printing needs,</p>
    <a class="read-more" href="#">Read More &gt;</a>
  </section>
</main>

<footer class="site-footer">
  <div class="footer-brand"><span class="brand-dot"></span>Harbourline<br>Press Works</div>
  <div class="footer-divider"></div>
  <address class="footer-address">
    <strong>Harbourline Press Works</strong><br>
    75 Quayside Lane East<br>
    Toronto, Ontario, M5X 2K9
    <span class="footer-email">E-mail: dorian@hpwdirect.example</span>
  </address>
  <div class="socials" aria-label="Social links"><span></span><span></span><span></span><span></span></div>
  <nav class="footer-nav">
    <a href="#">Home</a><i>|</i><a href="#">About Us</a><i>|</i><a href="#">Services</a><i>|</i><a href="#">Email a File</a><i>|</i><a href="#">Contact</a>
  </nav>
  <p class="copyright">Copyright © 2013 <strong>Harbourline Press Works</strong>. All rights reserved.</p>
</footer>
</body>
</html>
```